Commercial wall and ceiling contractor needs website

Construction trade companies are notoriously behind the rest of the world when it comes to using current technology to run their businesses; we are not one of those companies. We are a walls and ceilings contractor using up to date communications technologies and applying them unlike any other in our trade. As simple as it sounds, and it really is that simple, it is still a new idea in the trade. We are moving our customers towards communicating with us through a single point of contact using text and email; we distribute information to the appropriate internal party on our end. We need a website that generally appears traditionally familiar to the visitor while also expresses a fresh new approach and edginess to the trade business.

Target Market(s)

General contractors looking to get a bit of background info before inviting us to bid on their projects. This is not a high traffic environment. Their subsequent site visits will be primarily for contact info.

Industry/Entity Type

Construction Company

Number of Pages Required

3 page

Font styles to use
Sans Serif

Requirements
Must have
• The file I uploaded named "kolsite.docx" does not have to appear on the site in the same manner in which appears in the document file; but the info contained within that document does need to be represented on the site.

```html
<!DOCTYPE html>
<html lang="en">
<head>
<meta charset="utf-8">
<title>Stratafin Walls and Ceilings</title>
<link href="https://fonts.googleapis.com/css2?family=Roboto:wght@300;400;700&display=swap" rel="stylesheet">
<style>
:root{
  --green:#0b6340;
  --teal:#16977a;
  --gold:#b3872a;
  --text:#555;
  --dark:#333;
  --line:#ddd;
  --footer:#f2f2f2;
}
*{margin:0;padding:0;box-sizing:border-box}
html,body{width:721px;height:1200px;overflow:hidden;background:#fff}
body{position:relative;font-family:"Roboto",Arial,sans-serif;color:var(--text);font-weight:300}
.abs{position:absolute}
.topbar{left:0;top:0;width:721px;height:20px;background:var(--green);border-bottom:1px solid #0a4f33;color:#fff;font-size:8.5px;font-weight:400}
.topbar .contact{left:108px;top:4px;display:flex;gap:14px;align-items:center}
.topbar .contact span{display:flex;align-items:center;gap:4px}
.social{display:flex;gap:5px}
.social i{display:block;width:12px;height:12px;border:1px solid currentColor;border-radius:50%}
.topbar .social{left:545px;top:4px;color:#fff}
.brand{display:flex;align-items:center;gap:5px;color:var(--gold);font-weight:700;font-size:11px;letter-spacing:1.5px}
.brand b{display:block;width:14px;height:14px;border:2px solid var(--green)}
.header .brand{left:110px;top:36px}
.menu{font-size:7.5px;color:var(--dark);font-weight:400;white-space:nowrap}
.menu span{position:absolute;top:0}
.header .menu{left:0;top:46px}
.search{left:479px;top:38px;width:131px;height:18px;border:1px solid #bbb;font-size:6.5px;color:#aaa;padding:5px 4px}
.search svg{position:absolute;right:5px;top:4px}
.hero{left:0;top:67px;width:721px;height:257px;background:linear-gradient(180deg,#e6ecea 0%,#f4f6f5 50%,#dfe6df 100%)}
.hero .plant{left:0;top:110px;width:110px;height:147px;background:linear-gradient(180deg,#7aa863,#3e7a33)}
.hero .window{left:620px;top:150px;width:101px;height:107px;background:linear-gradient(180deg,#b7c7a6,#6f8f5c)}
.headline{font-size:23.5px;font-weight:400;color:#4a4a4a;line-height:32px;white-space:nowrap}
.hero .l1{left:130px;top:30px}
.hero .l2{left:181px;top:62px}
.hero .sub{left:133px;top:100px;width:440px;font-size:16px;line-height:22px;color:#555;font-weight:300}
.dots{left:344px;top:200px;display:flex;gap:3px}
.dots i{width:6px;height:6px;border-radius:50%;background:#f2b27a}
.dots i:first-child{background:#c7731f}
.card{left:103px;top:281px;width:513px;height:501px;background:#fff;box-shadow:0 2px 5px rgba(0,0,0,.18)}
.card h2{position:absolute;top:14px;width:100%;text-align:center;font-weight:400;font-size:19px;color:#555}
.intro{left:20px;top:48px;width:476px;font-size:9.4px;line-height:13.5px}
.intro p{margin-bottom:12px}
.stat-panel{top:188px;width:215px;height:125px;border-radius:4px;background:radial-gradient(circle at 50% 50%,#e4e4e4 0%,#eef3f2 45%,#fff 75%)}
.stat-panel.left{left:22px}.stat-panel.right{left:279px}
.col{top:340px;width:218px;font-size:9.2px;line-height:13.5px;text-align:justify;hyphens:auto;-webkit-hyphens:auto}
.col.left{left:22px}.col.right{left:279px}
.cta{left:19px;top:471px;width:490px;color:var(--teal);font-size:11.5px;font-weight:400;letter-spacing:.3px}
.cta span{position:absolute;white-space:nowrap}
.projects-title{left:0;top:816px;width:721px;text-align:center;font-size:19px;font-weight:400;color:#555}
.proj{width:118px;height:113px;box-shadow:0 1px 3px rgba(0,0,0,.15);background:#fff}
.proj .photo{height:79px}
.ph-a{background:linear-gradient(135deg,#d9cfbf,#b9ab93 60%,#8f8a78)}
.ph-b{background:linear-gradient(135deg,#e9e7e3,#cfc7bd 60%,#5a463a)}
.ph-c{background:linear-gradient(135deg,#8ea77e,#c8c6c0 50%,#4a4440)}
.ph-d{background:linear-gradient(135deg,#bdbab4,#8b7d6d 55%,#3a332c)}
.proj h3{font-size:7.5px;font-weight:400;color:var(--green);margin:8px 0 0 9px}
.proj p{font-size:7px;margin:4px 0 0 9px}
.footer{left:0;top:1122px;width:721px;height:78px;background:var(--footer);border-top:2px solid #ccc}
.footer .brand{left:114px;top:26px}
.footer .menu{left:0;top:31px;color:#444}
.footer .social{left:545px;top:30px;color:#bbb}
.footer .rule{left:103px;top:56px;width:513px;height:1px;background:#ccc}
.footer .copy{left:486px;top:64px;font-size:6.2px;color:#555;font-weight:400}
</style>
</head>
<body>

<div class="abs topbar">
  <div class="abs contact">
    <span><svg width="11" height="11" viewBox="0 0 12 12"><circle cx="6" cy="6" r="5.4" fill="none" stroke="#fff" stroke-width=".8"/><path d="M4 3.3l1 1.3-.6.7c.4.9 1.1 1.6 2 2l.7-.6 1.3 1-.6 1C5.7 8.6 3.4 6.3 3.4 4z" fill="#fff"/></svg>: 604-555-0182</span>
    <span><svg width="11" height="11" viewBox="0 0 12 12"><circle cx="6" cy="6" r="5.4" fill="none" stroke="#fff" stroke-width=".8"/><rect x="3" y="4" width="6" height="4" fill="none" stroke="#fff" stroke-width=".7"/><path d="M3 4l3 2.2L9 4" fill="none" stroke="#fff" stroke-width=".7"/></svg>: hello@stratafinwalls.com</span>
  </div>
  <div class="abs social"><i></i><i></i><i></i><i></i></div>
</div>

<header class="header">
  <div class="abs brand"><b></b>STRATAFIN</div>
  <nav class="abs menu"><span style="left:294px">Home</span><span style="left:333px">Projects ▾</span><span style="left:379px">Services ▾</span><span style="left:427px">Contact Us</span></nav>
  <div class="abs search">Search...
    <svg width="9" height="9" viewBox="0 0 10 10"><circle cx="4" cy="4" r="3.2" fill="none" stroke="#777" stroke-width=".8"/><path d="M6.4 6.4L9.4 9.4" stroke="#777" stroke-width=".9"/></svg>
  </div>
</header>

<section class="abs hero">
  <div class="abs plant" role="img" aria-label="Potted plant in a bright interior"></div>
  <div class="abs window" role="img" aria-label="Garden view through large windows"></div>
  <h1 class="abs headline l1">CONTACT US FOR BEST RESULTS</h1>
  <div class="abs headline l2">AND 100% SATISFACTION OF JOB</div>
  <p class="abs sub">we distribute information to the appropriate internal party on our end.</p>
  <div class="abs dots"><i></i><i></i><i></i><i></i></div>
</section>

<section class="abs card">
  <h2>Why choose Stratafin?</h2>
  <div class="abs intro">
    <p>Today’s communication landscape is dramatically different than it was a mere ten years ago.  We use our phones less and less for making calls.  In fact, it is reported that 70% of direct communication is through text messaging, not phone calls; with text messaging increasing in use by %7,700 since 2008.<br>No surprise here.</p>
    <p>Think of the phone call process; auto attendant, “...choose 1 for...”, “...if you know the extension...”, “...spell the name...”, “...to hear a directory...”, etc.; ugh.  I don’t know about you but when I finally get to the person I want to speak with, I often forget why I called in the first place.  And let’s not get started on voicemail; I mean really, who likes leaving a voice message let alone retrieving one.</p>
  </div>

  <div class="abs stat-panel left" role="img" aria-label="Infographic on texting speed and response times compared with phone calls"></div>
  <div class="abs stat-panel right" role="img" aria-label="Infographic on consumer and business attitudes to texting"></div>

  <p class="abs col left">The average length of a phone call has sharply decreased since 2006.  That’s because it’s easier to swap a bunch of short messages than it is to interrupt each other’s work at hand with a phone call.  Furthermore, 99% of text messages are read while only 33% of voicemail messages are heard; 95% of text messages are read within 3 minutes and, on average, responded to within 90 seconds.</p>
  <p class="abs col right">One of the many ways that Stratafin is bringing technology to its trade is through communication tools.  A single point of contact gets you where you want to go.  We distribute the text and email internally.  Not only that, we share equal access to our communication points to hold each other accountable for their respective responsibilities.  This flow of information is a more efficient, effective, and direct.</p>

  <div class="abs cta">
    <span style="left:0">Try it now!&nbsp;&nbsp;&nbsp;TEXT</span>
    <span style="left:129px">604-555-0182</span>
    <span style="left:246px">EMAIL: hello@stratafinwalls.com</span>
  </div>
</section>

<h2 class="abs projects-title">Recently Completed Projects</h2>

<article class="abs proj" style="left:103px;top:856px"><div class="photo ph-a" role="img" aria-label="Living room with sofas and tall windows"></div><h3>The Marigold Apt.</h3><p>India- Mumbai</p></article>
<article class="abs proj" style="left:234px;top:856px"><div class="photo ph-b" role="img" aria-label="White living room with fireplace"></div><h3>The Marigold Apt.</h3><p>India- Mumbai</p></article>
<article class="abs proj" style="left:366px;top:856px"><div class="photo ph-c" role="img" aria-label="Stone feature wall with television"></div><h3>The Marigold Apt.</h3><p>India- Mumbai</p></article>
<article class="abs proj" style="left:497px;top:856px"><div class="photo ph-d" role="img" aria-label="Double height lounge with stone wall"></div><h3>The Marigold Apt.</h3><p>India- Mumbai</p></article>
<article class="abs proj" style="left:103px;top:981px"><div class="photo ph-a" role="img" aria-label="Living room with sofas and tall windows"></div><h3>The Marigold Apt.</h3><p>India- Mumbai</p></article>
<article class="abs proj" style="left:234px;top:981px"><div class="photo ph-b" role="img" aria-label="White living room with fireplace"></div><h3>The Marigold Apt.</h3><p>India- Mumbai</p></article>
<article class="abs proj" style="left:366px;top:981px"><div class="photo ph-c" role="img" aria-label="Stone feature wall with television"></div><h3>The Marigold Apt.</h3><p>India- Mumbai</p></article>
<article class="abs proj" style="left:497px;top:981px"><div class="photo ph-d" role="img" aria-label="Double height lounge with stone wall"></div><h3>The Marigold Apt.</h3><p>India- Mumbai</p></article>

<footer class="abs footer">
  <div class="abs brand"><b></b>STRATAFIN</div>
  <nav class="abs menu"><span style="left:277px">Home</span><span style="left:317px">Projects</span><span style="left:363px">Services</span><span style="left:411px">Contact Us</span></nav>
  <div class="abs social"><i></i><i></i><i></i><i></i></div>
  <div class="abs rule"></div>
  <p class="abs copy">Copyright © 2019 Stratafin. All rights reserved.</p>
</footer>

</body>
</html>
```